Birchmoor Yard Care_2015 New Cards_V1

We need an enhanced business card from what we have today. We are a Landscaping company and we have an existing Logo and text info that we would like to include.
Text to include:
In business for over 20 years,Fully Insured, Weekly Lawn Maintenance, Spring & Fall Clean-up, Todd Pierson, 203-555-0147, www.birchmooryardcarect.example, Visit our Website for additional Lawn Care Services or email directly at TODD@BIRCHMOORYARDCARE.EXAMPLE, We appreciate your business.
We want full color background and we will want to take this design and work with a printer that does high graphic silk screen cards. The colors we have thought about are Black, with our Green Logo, with Gold Text...we are open to different colors, we just want the card to wow!

Target Market(s)

Lawn Care Maintenance

Industry/Entity Type

Lawn Care

Contact Information for Business Card

Text to include:
In business for over 20 years, Fully Insured, Weekly Lawn Maintenance, Spring & Fall Clean-up, Todd Pierson, 203-555-0147, www.birchmooryardcarect.example, Visit our Website for additional Lawn Care Services or email directly at TODD@BIRCHMOORYARDCARE.EXAMPLE, We appreciate your business.

Requirements
Must have
• Logo, text details about how to reach us, standard size business cards that go horizontal.
Nice to have
• background colors, background designs, raised embossed lettering, rounded corners(2 or 4),

```html
<!DOCTYPE html>
<html lang="en">
<head>
<meta charset="utf-8">
<title>Birchmoor Yard Care – Business Cards</title>
<link href="https://fonts.googleapis.com/css2?family=Open+Sans:ital,wght@0,400;0,600;0,700;1,400;1,600&display=swap" rel="stylesheet">
<style>
  :root {
    --backdrop: #2b2d30;
    --forest: #0b3d12;
    --forest-deep: #08330e;
    --card-white: #f7f7f7;
    --ink-green: #0d3f14;
    --ink-grey: #555a5e;
    --ink-dark: #2a2c2e;
    --rule: #bfc2c4;
    --on-green: #ffffff;
  }
  * { margin: 0; padding: 0; box-sizing: border-box; }
  html, body {
    width: 1200px; height: 864px; overflow: hidden;
    background: var(--backdrop);
    font-family: "Open Sans", Arial, sans-serif;
  }
  .canvas { position: relative; width: 1200px; height: 864px; }

  .card { position: absolute; box-shadow: 0 6px 18px rgba(0,0,0,.45); }

  /* Back of card */
  .card-back {
    left: 205px; top: 70px; width: 540px; height: 308px;
    background: linear-gradient(135deg, var(--forest) 0%, var(--forest-deep) 100%);
    color: var(--on-green);
  }
  .feature-list {
    position: absolute; left: 66px; top: 74px;
    list-style: none; font-style: italic; font-weight: 600; font-size: 14px; line-height: 25px;
  }
  .feature-list li { position: relative; padding-left: 20px; }
  .feature-list li::before {
    content: ""; position: absolute; left: 2px; top: 8px;
    width: 8px; height: 8px; border-radius: 50%; background: var(--on-green);
  }
  .brand-name-back {
    position: absolute; left: 318px; top: 136px; width: 200px;
    font-weight: 700; font-size: 19px; line-height: 24px; color: var(--on-green);
    text-align: center; white-space: nowrap;
  }
  .back-note {
    position: absolute; left: 40px; right: 40px; top: 222px;
    text-align: center; font-style: italic; font-weight: 600; font-size: 14px; line-height: 21px;
  }

  /* Front of card */
  .card-front {
    left: 190px; top: 410px; width: 640px; height: 366px;
    background: var(--card-white);
  }
  .brand-name-front {
    position: absolute; right: 44px; top: 80px;
    font-weight: 700; font-size: 28px; color: var(--ink-green); white-space: nowrap;
  }
  .holder { position: absolute; left: 78px; top: 104px; }
  .holder-name { font-weight: 600; font-size: 21px; color: var(--ink-green); line-height: 24px; }
  .holder-title { font-size: 14px; color: var(--ink-grey); }
  .divider {
    position: absolute; left: 78px; right: 44px; top: 178px;
    border-top: 1px solid var(--rule);
  }
  .contact-list {
    position: absolute; right: 44px; top: 214px; list-style: none;
    font-size: 15px; line-height: 24px; color: var(--ink-dark); text-align: right;
  }
  .contact-list li { display: flex; justify-content: flex-end; align-items: center; gap: 8px; }
  .contact-icon { width: 13px; height: 13px; fill: var(--ink-green); stroke: var(--ink-green); }
</style>
</head>
<body>
<main class="canvas">

  <section class="card card-back" aria-label="Card back">
    <ul class="feature-list">
      <li>In business for over 20 years</li>
      <li>Fully Insured</li>
      <li>Weekly Lawn Maintenance</li>
      <li>Spring &amp; Fall Clean-up</li>
    </ul>
    <div class="brand-name-back">Birchmoor Yard Care</div>
    <p class="back-note">Visit our Website for additional Lawn Care Services or email<br>directly at TODD@BIRCHMOORYARDCARE.EXAMPLE</p>
  </section>

  <section class="card card-front" aria-label="Card front">
    <div class="brand-name-front">Birchmoor Yard Care</div>
    <div class="holder">
      <div class="holder-name">Daniel Brooks</div>
      <div class="holder-title">Managing Director</div>
    </div>
    <div class="divider"></div>
    <ul class="contact-list">
      <li>044-555-0183
        <svg class="contact-icon" viewBox="0 0 16 16" aria-hidden="true"><path stroke="none" d="M3 1l3 3-1.5 2a9 9 0 0 0 5.5 5.5L12 10l3 3-2 2C7 15 1 9 1 3z"/></svg></li>
      <li>123-555-0162
        <svg class="contact-icon" viewBox="0 0 16 16" aria-hidden="true"><rect stroke="none" x="1" y="6" width="14" height="8" rx="1"/><rect fill="none" stroke-width="1.5" x="4" y="2" width="8" height="5"/></svg></li>
      <li>123-555-0162
        <svg class="contact-icon" viewBox="0 0 16 16" aria-hidden="true"><rect fill="none" stroke-width="1.8" x="4" y="1" width="8" height="14" rx="1.5"/><circle stroke="none" cx="8" cy="12.5" r="1"/></svg></li>
      <li>info@mailbox.example
        <svg class="contact-icon" viewBox="0 0 16 16" aria-hidden="true"><rect stroke="none" x="1" y="3" width="14" height="10"/><path fill="none" stroke="#f7f7f7" stroke-width="1.3" d="M1 3l7 6 7-6"/></svg></li>
      <li>www.yoursite.example
        <svg class="contact-icon" viewBox="0 0 16 16" aria-hidden="true"><path fill="none" stroke-width="2" d="M7 9l-2.5 2.5a2 2 0 0 1-3-3L4 6M9 7l2.5-2.5a2 2 0 0 1 3 3L12 10M6 10l4-4"/></svg></li>
    </ul>
  </section>

</main>
</body>
</html>
```